Fin-Tech Firm Captivating Business Card Design

We need a logo design as well to compliment this business card.

We are a new startup based in Singapore called 'Quorvane Systems'.

We develop an array of financial solutions ranging from payment convenience to forex trading and remittance.

Our initial product is Pam - an application which allows user to pre-order food items which would be ready for pickup upon arrival.

We would like to see designs being in black and silver or whatever that looks appealing and exudes a fun and professional feel.

We're not picky as long as it doesn't look like common business cards will do.

I do have a current logo which i do not really like. It will be attached for reference sake

Info:

Quorvane Systems Pte. Ltd.
Company Registration no. 208817264K

FILE TO BE IN .AI and .PSD

Target Market(s)

-F&B (Online-Ordering)
-Finance(P2P Lending and Forex)

Industry/Entity Type

Finance

Contact Information for Business Card

Name
Position
Contact
Email
Address: 47 Bexley Lane, Harbourvale Tower, #14-03 Singapore 068215

Marcus Teo
Founder, Managing Director
+65 98471630
marcus.t@quorvanesys.com

Wei Lok
Founder, Executive Director
+65 96058243
wei.l@quorvanesys.com

Logo Text

Quorvane Systems

Font styles to use
Sans Serif

Requirements
Must have
• Something that has word play about link lynk
• Minimalistic but also something that catches The Eye
• Gold/silver on white/black might be nice
• Animal logo ; horse, eagle, bull or bear
Nice to have
• Just make it look fun and cute
• Just a suggestion to make the Y of quorvane stand out
Should not have
• Any landmarks of singapore
• Exclude Pte. Ltd.

```html
<!DOCTYPE html>
<html lang="en">
<head>
<meta charset="UTF-8">
<title>Quorvane Systems — Business Card</title>
<link href="https://fonts.googleapis.com/css2?family=Questrial&display=swap" rel="stylesheet">
<style>
  :root {
    --backdrop: #e6e6e4;
    --card: #141414;
    --card-edge: #0c0c0c;
    --ink: #e4e4e4;
    --ink-soft: #bdbdbd;
    --silver: #cfcfcf;
    --accent: #e58a1f;
  }
  html, body {
    margin: 0;
    padding: 0;
    width: 1200px;
    height: 1021px;
    overflow: hidden;
    background: var(--backdrop);
  }
  .canvas {
    position: relative;
    width: 1200px;
    height: 1021px;
    font-family: "Questrial", "Century Gothic", sans-serif;
  }
  .card {
    position: absolute;
    left: 290px;
    width: 620px;
    height: 360px;
    background: var(--card);
    box-shadow: 0 2px 0 var(--card-edge), 0 18px 40px rgba(0,0,0,0.22);
    box-sizing: border-box;
  }
  .card--contact { top: 110px; }
  .card--brand { top: 550px; }

  .brand-mark {
    position: absolute;
    top: 40px;
    right: 44px;
    display: flex;
    align-items: center;
    gap: 10px;
    color: var(--accent);
    font-size: 17px;
    letter-spacing: 0.08em;
  }
  .brand-mark .dot {
    width: 10px;
    height: 10px;
    border-radius: 50%;
    background: var(--accent);
  }

  .contact-block {
    position: absolute;
    left: 52px;
    bottom: 52px;
    color: var(--ink);
  }
  .contact-name {
    font-size: 27px;
    margin: 0 0 6px;
    font-weight: 400;
    letter-spacing: 0.01em;
  }
  .contact-role {
    font-size: 15px;
    color: var(--ink-soft);
    margin: 0 0 14px;
  }
  .contact-list {
    list-style: none;
    margin: 0;
    padding: 0;
    font-size: 15px;
    line-height: 1.45;
  }
  .contact-list li {
    display: flex;
    align-items: flex-start;
    gap: 12px;
  }
  .contact-list svg {
    width: 14px;
    height: 14px;
    margin-top: 3px;
    flex: none;
    fill: var(--ink);
  }

  .wordmark {
    position: absolute;
    left: 0;
    right: 0;
    top: 0;
    bottom: 0;
    display: flex;
    flex-direction: column;
    align-items: center;
    justify-content: center;
    gap: 22px;
    color: var(--silver);
  }
  .wordmark .dot {
    width: 26px;
    height: 26px;
    border-radius: 50%;
    background: var(--accent);
  }
  .wordmark-name {
    font-size: 44px;
    letter-spacing: 0.16em;
    text-transform: uppercase;
    text-align: center;
    line-height: 1.15;
  }
</style>
</head>
<body>
<main class="canvas">

  <section class="card card--contact" aria-label="Business card, contact side">
    <div class="brand-mark"><span class="dot"></span><span>Quorvane</span></div>

    <div class="contact-block">
      <h1 class="contact-name">Marcus Teo</h1>
      <p class="contact-role">Founder, Managing Director</p>
      <ul class="contact-list">
        <li>
          <svg viewBox="0 0 16 16" aria-hidden="true"><path d="M3 1.5l3 .5 1 3.2-1.8 1.2a8.5 8.5 0 0 0 4.4 4.4l1.2-1.8 3.2 1 .5 3c-.3 1-1.3 1.5-2.3 1.5C6.2 14.5 1.5 9.8 1.5 3.8c0-1 .5-2 1.5-2.3z"/></svg>
          <span>+65 98471630</span>
        </li>
        <li>
          <svg viewBox="0 0 16 16" aria-hidden="true"><path d="M1 3.5h14v9H1z M1.8 4.2L8 9l6.2-4.8" fill="none" stroke="currentColor"/><path d="M1 3.5h14v1L8 9.6 1 4.5z"/><rect x="1" y="3.5" width="14" height="9" fill="none" stroke="#e4e4e4" stroke-width="1.2"/></svg>
          <span>marcus.t@quorvanesys.com</span>
        </li>
        <li>
          <svg viewBox="0 0 16 16" aria-hidden="true"><path d="M8 1a5 5 0 0 0-5 5c0 3.6 5 9 5 9s5-5.4 5-9a5 5 0 0 0-5-5zm0 7a2 2 0 1 1 0-4 2 2 0 0 1 0 4z"/></svg>
          <span>47 Bexley Lane, Harbourvale Tower<br>#14-03 Singapore 068215</span>
        </li>
      </ul>
    </div>
  </section>

  <section class="card card--brand" aria-label="Business card, brand side">
    <div class="wordmark">
      <span class="dot"></span>
      <span class="wordmark-name">Quorvane<br>Systems</span>
    </div>
  </section>

</main>
</body>
</html>
```